Tindle PR (young, fun PR agency) needs a Business Card Design

We need a new business card design that reflects who we are as a company. We're a Sydney-based PR agency that's six years old with clients including Blue Heron, Wavecrest, OVERA, Joe Calloway etc. - just check out our website for more info: www.tindlepr.com.au. We would like to see designs that bring to life our company name and what we do (generating media coverage for brands on TV, radio, online and in newspapers and magazines). We don't want a corporate style card but one that people take notice of and think 'wow that's a cool business card'. It doesn't have to be the standard rectangle shape and can incorporate humour.

Target Market(s)

Clients (generally cool/creative types) and media

Industry/Entity Type

Business

Requirements
Must have
• The card must feature our business logo (which can be updated if you like) and use both sides.
Nice to have
• The card could feature a cool illustration

```html
<!DOCTYPE html>
<html lang="en">
<head>
<meta charset="utf-8">
<title>Tindle PR — Business Card</title>
<link rel="stylesheet" href="https://fonts.googleapis.com/css2?family=Arimo:wght@700&family=Tinos&display=swap">
<style>
  :root {
    --backdrop: #3b3b3b;
    --card-white: #ffffff;
    --brand-orange: #f5ac4f;
    --ink: #1a1a1a;
    --shadow: rgba(0, 0, 0, 0.45);
  }
  * { margin: 0; padding: 0; box-sizing: border-box; }
  html, body {
    width: 1200px;
    height: 569px;
    overflow: hidden;
    background: var(--backdrop);
  }
  .stage {
    position: relative;
    width: 1200px;
    height: 569px;
  }
  .card {
    position: absolute;
    top: 140px;
    height: 285px;
    overflow: hidden;
    box-shadow: 2px 4px 10px var(--shadow);
    color: var(--ink);
    font-family: "Arimo", Arial, sans-serif;
    font-weight: 700;
  }
  .card--front {
    left: 82px;
    width: 515px;
    background: var(--card-white);
  }
  .card--back {
    left: 632px;
    width: 517px;
    background: var(--brand-orange);
  }
  .card__disc {
    position: absolute;
    top: 0;
    left: 0;
    width: 515px;
    height: 285px;
  }

  .person {
    position: absolute;
    left: 26px;
    top: 16px;
    font-size: 11.5px;
    line-height: 16px;
  }
  .wordmark {
    position: absolute;
    left: 28px;
    top: 112px;
    display: flex;
    align-items: center;
    gap: 14px;
  }
  .wordmark__name {
    font-size: 34px;
    letter-spacing: 0.5px;
    line-height: 1;
    color: var(--ink);
  }
  .wordmark__circle {
    width: 52px;
    height: 52px;
    border: 2px solid var(--ink);
    border-radius: 50%;
  }
  .tagline {
    position: absolute;
    left: 25px;
    top: 236px;
    max-width: 340px;
    white-space: nowrap;
    font-family: "Tinos", "Times New Roman", serif;
    font-weight: 400;
    font-size: 15px;
  }
  .contact {
    position: absolute;
    right: 22px;
    top: 95px;
    list-style: none;
    text-align: right;
    font-size: 11.5px;
    line-height: 16px;
  }
</style>
</head>
<body>
<main class="stage">
  <section class="card card--front" aria-label="Card front">
    <svg class="card__disc" viewBox="0 0 515 285" aria-hidden="true">
      <circle cx="515" cy="142.5" r="140" fill="var(--brand-orange)" stroke="var(--ink)" stroke-width="5"/>
    </svg>
    <p class="person">Daniel K. Marlow, PhD MBA<br>Founding Principal</p>
    <div class="wordmark">
      <span class="wordmark__name">TINDLE PR</span>
      <span class="wordmark__circle"></span>
    </div>
    <p class="tagline">"Putting your brand on TV, radio, online and in print"</p>
  </section>

  <section class="card card--back" aria-label="Card back">
    <svg class="card__disc" viewBox="0 0 515 285" aria-hidden="true">
      <circle cx="0" cy="142.5" r="140" fill="var(--card-white)" stroke="var(--ink)" stroke-width="5"/>
    </svg>
    <ul class="contact">
      <li>Meridian GenCapital Inc</li>
      <li>418 Harbor Street</li>
      <li>Lakeview, NY 10482</li>
      <li>212-555-0148</li>
      <li>dkmarlow@meridiangencapital.com</li>
      <li>www.meridiangencapital.com</li>
    </ul>
  </section>
</main>
</body>
</html>
```